Quillon Maison Wood Fired Pizza business card design

I have a logo and need an eye catching design that will get me noticed.
My business is wood fired pizza. I want a bold design that will make our customers remember us and the food that we serve. Work with the colors of our logo and texts. Maybe add designs that lend to what or how pizza is made using our wood fired oven?

Target Market(s)

Foodies!

Contact Information for Business Card

Quillon Maison Wood Fired Pizza
Our slogan is Fast. Fresh. Handcrafted
Catering for all events

Requirements
Must have
• Dana Porrick
Telephone 570 555 0183
website www.getquillon.example
Facebook @getquillonpizza maybe use the facebook logo next to it
Instagram getquillonpizza maybe use the instagram logo next to it
Catering for all events
Nice to have
• Maybe pizza peels, pizza cutters? Wood? Fired wood? Using our flame in the background?
Please work with different colored text so each sentence stands out? A themed color for facebook?
Maybe work with the colors within our logo?
Please try to use the our quillon font, but not a must have.

```html
<!DOCTYPE html>
<html lang="en">
<head>
<meta charset="utf-8">
<title>Quillon Maison Wood Fired Pizza – Business Card</title>
<link href="https://fonts.googleapis.com/css2?family=Bebas+Neue&family=Oswald:wght@400;500;600&display=swap" rel="stylesheet">
<style>
  :root{
    --page:#1a1a1a;
    --card:#1f1e1d;
    --card-deep:#181716;
    --texture:#3a2f26;
    --texture-soft:#2c2520;
    --orange:#f0901e;
    --red:#d3242a;
    --white:#f2f2f2;
  }
  *{margin:0;padding:0;box-sizing:border-box}
  html,body{width:1200px;height:750px;overflow:hidden;background:var(--page)}
  .canvas{position:relative;width:1200px;height:750px}

  .card{position:absolute;top:139px;width:270px;height:472px;overflow:hidden;
        box-shadow:0 18px 40px rgba(0,0,0,.55);text-align:center;color:var(--white)}
  .card--front{left:295px}
  .card--back{left:637px}

  .card__texture{position:absolute;inset:0;
        background:
          radial-gradient(circle at 78% 16%,var(--texture) 0,transparent 30%),
          radial-gradient(circle at 20% 86%,var(--texture) 0,transparent 30%),
          radial-gradient(circle at 8% 40%,var(--texture-soft) 0,transparent 18%),
          radial-gradient(circle at 94% 62%,var(--texture-soft) 0,transparent 18%),
          radial-gradient(circle at 30% 8%,var(--texture-soft) 0,transparent 14%),
          radial-gradient(circle at 72% 94%,var(--texture-soft) 0,transparent 14%),
          linear-gradient(160deg,var(--card),var(--card-deep))}
  .card__content{position:relative;height:100%}

  .brand{position:absolute;left:0;right:0;display:flex;flex-direction:column;align-items:center}
  .brand__dot{border-radius:50%;background:var(--red)}
  .brand__name{font-family:"Oswald",sans-serif;font-weight:600;color:var(--white);line-height:1}
  .card--front .brand{top:56px}
  .card--front .brand__dot{width:86px;height:86px;margin-bottom:20px}
  .card--front .brand__name{font-size:20px;letter-spacing:.14em;padding-left:.14em}
  .card--back .brand{top:92px}
  .card--back .brand__dot{width:124px;height:124px;margin-bottom:38px}
  .card--back .brand__name{font-size:27px;letter-spacing:.1em;padding-left:.1em}

  .person{position:absolute;top:228px;left:0;right:0}
  .person__name{font-family:"Bebas Neue",sans-serif;font-size:28px;color:var(--orange);letter-spacing:.12em;line-height:1;padding-left:.12em}
  .person__role{font-family:"Oswald",sans-serif;font-weight:500;font-size:16px;letter-spacing:.3em;margin-top:4px;padding-left:.3em;line-height:1}

  .contacts{position:absolute;top:290px;left:0;right:0;list-style:none}
  .contact{display:flex;flex-direction:column;align-items:center;height:38px}
  .contact__icon{width:15px;height:15px;border:1.2px solid var(--orange);border-radius:50%;
        display:flex;align-items:center;justify-content:center;margin-bottom:4px}
  .contact__icon svg{width:8px;height:8px}
  .contact__icon--social::after{content:"";width:7px;height:7px;border-radius:50%;background:var(--orange)}
  .contact__text{font-family:"Oswald",sans-serif;font-size:14px;letter-spacing:.22em;line-height:1.2;padding-left:.22em;text-transform:uppercase}

  .slogan{position:absolute;top:313px;left:0;right:0;font-family:"Bebas Neue",sans-serif;line-height:1}
  .slogan__main{font-size:24px;letter-spacing:.04em;color:var(--white)}
  .slogan__sub{font-size:18px;letter-spacing:.14em;color:var(--orange);margin-top:3px;padding-left:.14em}
</style>
</head>
<body>
<main class="canvas">

  <section class="card card--front" aria-label="Business card front">
    <div class="card__texture" role="img" aria-label="Faint sketched pizzas, tomatoes and herbs across the card"></div>
    <div class="card__content">
      <div class="brand">
        <span class="brand__dot"></span>
        <span class="brand__name">QUILLON MAISON</span>
      </div>
      <div class="person">
        <p class="person__name">Dana Porrick</p>
        <p class="person__role">OWNER</p>
      </div>
      <ul class="contacts">
        <li class="contact">
          <span class="contact__icon"><svg viewBox="0 0 10 10"><path d="M2 1 L3.6 1 L4.2 3 L3.2 3.8 Q4.2 5.8 6.2 6.8 L7 5.8 L9 6.4 L9 8 Q8.5 9 7 8.8 Q2 7.5 1.2 3 Q1 1.5 2 1Z" fill="var(--orange)"/></svg></span>
          <span class="contact__text">570 555 0183</span>
        </li>
        <li class="contact">
          <span class="contact__icon"><svg viewBox="0 0 10 10"><rect x="1" y="2.5" width="8" height="5.5" fill="var(--orange)"/><path d="M1 2.5 L5 5.6 L9 2.5" stroke="var(--card)" stroke-width="0.8" fill="none"/></svg></span>
          <span class="contact__text">getquillon.example</span>
        </li>
        <li class="contact">
          <span class="contact__icon contact__icon--social"></span>
          <span class="contact__text">@getquillonpizza</span>
        </li>
        <li class="contact">
          <span class="contact__icon contact__icon--social"></span>
          <span class="contact__text">getquillonpizza</span>
        </li>
      </ul>
    </div>
  </section>

  <section class="card card--back" aria-label="Business card back">
    <div class="card__texture" role="img" aria-label="Faint sketched pizzas, tomatoes and herbs across the card"></div>
    <div class="card__content">
      <div class="brand">
        <span class="brand__dot"></span>
        <span class="brand__name">QUILLON MAISON</span>
      </div>
      <div class="slogan">
        <p class="slogan__main">FAST. FRESH. HANDCRAFTED</p>
        <p class="slogan__sub">CATERING FOR ALL EVENTS</p>
      </div>
    </div>
  </section>

</main>
</body>
</html>
```